New Website for Crime Scene Cleaner required

I need someone to create a complete new website and can set up SEO for me through the Website Designer or a third party for me. I have Logo that i will upload shortly once finalized for the website. I have domain names already but will need to be registered by the winner(i can supply the details I have received from HostMarlo). I am looking for a website that stands out but is simple and elegant, easy to navigate and use yet not boring. Using information provided by me for wording to create it as a stand out website. in total i am looking at 5-7 pages (About/Home, Fire & Smoke Restoration, Water Restoration/Mould Remediation, Crime Scene Cleaners, Methamphetamine Remediation/ Testing Services, Hoarding & Squalor Cleaning, Contact Us/Testimonials)This will be a start to finish project. I would like assistance to have it set up user friendly on mobile devices etc or refer a third party who can assist. Must be able to provide ongoing support when required by myself if the successful winner (i understand this will be an additional fee if required in the future).
You will also require to assist me with the email set up for the website so that it is fully functional or provide a third party who can.
To gain some information about the business you can visit my old website at www.pelbrookcove.com.au and welcome to use some of the wording from there for your entry.
It's been 14yrs since i've had a website made from me so suggestions are welcome if not mentioned in the scope as I want the website to be great.

I have uploaded 2 Logo's and a 3D Logo will come through shortly.

Target Market(s)

People affected by a traumatic event in their lives needing assistance by professionals who are understanding and professionally trained

Coding

Coded - Design and coding required

Requirements
Must have
• *** Please note that correct wording for pages will only be supplied upon a successful winner for the finalization of the project.

I have domain names already but will need to be registered by the winner(i can supply the details I have received from HostMarlo).
Nice to have
• the feeling that we care because we do and that we are passionate for what we do.

```html
<!DOCTYPE html>
<html lang="en">
<head>
<meta charset="utf-8">
<title>Haven &amp; Restore Services</title>
<link href="https://fonts.googleapis.com/css2?family=Poppins:wght@300;400;500;600;700&family=Bebas+Neue&display=swap" rel="stylesheet">
<style>
:root{
  --orange:#f26522;
  --orange-light:#f7931e;
  --ink:#1d2731;
  --text:#444b52;
  --muted:#7a7f85;
  --grey-bg:#f5f6f8;
  --line:#e4e6e9;
  --white:#ffffff;
  --footer:#1b2430;
}
*{margin:0;padding:0;box-sizing:border-box}
html,body{width:1200px;height:3600px;overflow:hidden}
body{font-family:'Poppins',sans-serif;color:var(--text);background:var(--white);position:relative}
.abs{position:absolute}
.grad{background:linear-gradient(90deg,var(--orange),var(--orange-light))}

/* header */
.site-header{left:0;top:0;width:1200px;height:94px;background:var(--white);border-top:3px solid var(--orange);z-index:3}
.brand{left:180px;top:22px;width:140px;text-align:center;font-weight:600;color:var(--orange);font-size:14px;line-height:1.2}
.brand small{display:block;font-size:8px;letter-spacing:3px;color:var(--muted);font-weight:400}
.brand-dot{display:inline-block;width:26px;height:26px;border-radius:50%;background:var(--orange);margin-bottom:4px}
.main-nav{left:515px;top:31px;display:flex;gap:28px;font-size:11px;color:var(--ink);letter-spacing:.3px}
.main-nav .active{color:var(--orange)}
.call-box{left:989px;top:0;width:211px;height:74px}
.call-icon{left:966px;top:14px;width:46px;height:46px;border-radius:50%;background:var(--white);border:2px solid var(--orange);display:flex;align-items:center;justify-content:center}
.call-box .lbl{position:absolute;left:42px;top:18px;font-size:9px;color:var(--white)}
.call-box .num{position:absolute;left:40px;top:34px;font-size:19px;font-weight:600;color:var(--white)}

/* hero */
.hero{left:0;top:94px;width:1200px;height:618px;background:linear-gradient(100deg,#8f8a82 0%,#b7b0a5 35%,#6a6f5c 60%,#a9a49b 100%)}
.hero-badge{left:209px;top:225px;width:344px;height:344px;border-radius:50%;background:rgba(242,101,34,.92);text-align:center;color:var(--white)}
.hero-badge .pre{margin-top:88px;font-size:22px;font-weight:300}
.hero-badge .pre b{font-weight:700}
.hero-badge h1{font-family:'Bebas Neue',sans-serif;font-weight:400;font-size:46px;line-height:44px;margin-top:10px;letter-spacing:.5px}
.btn{display:inline-block;border-radius:24px;color:var(--white);font-weight:500;text-transform:uppercase;text-align:center}
.hero-badge .btn{margin-top:16px;width:150px;height:40px;line-height:40px;font-size:14px;background:var(--orange-light)}
.hero-arrows{left:344px;top:670px}

/* services */
.sec-title{width:1200px;left:0;text-align:center;color:var(--orange);font-weight:500;font-size:34px;letter-spacing:.5px}
.sec-sub{width:1200px;left:0;text-align:center;font-size:12.5px;line-height:21px;color:var(--ink)}
.service{width:170px;text-align:center;font-size:13px;line-height:18px;color:var(--ink)}
.service .ring{width:76px;height:76px;margin:0 auto 12px;border-radius:50%;background:var(--white);box-shadow:0 2px 10px rgba(0,0,0,.12);display:flex;align-items:center;justify-content:center}
.service .ring span{width:44px;height:44px;border-radius:50%;background:#fde6d8}
.service.on .ring{border:2px solid var(--orange)}
.services-rule{left:168px;top:1076px;width:849px;height:1px;background:var(--line)}
.services-active{left:210px;top:1075px;width:55px;height:3px;background:var(--orange)}

.feature-img{left:562px;top:1132px;width:401px;height:299px;border-radius:0 20px 0 0;background:linear-gradient(160deg,#4a3a2e,#2a221d 50%,#6b5a48)}
.feature-tag{left:634px;top:1180px;width:260px;height:40px;background:#b8191e;color:var(--white);font-family:'Bebas Neue',sans-serif;font-size:38px;line-height:42px;text-align:center}
.feature-card{left:254px;top:1225px;width:361px;height:194px;background:var(--white);border-top:3px solid var(--orange);box-shadow:0 4px 18px rgba(0,0,0,.08);padding:38px 40px 0 42px}
.feature-card h3{font-size:21px;font-weight:500;color:var(--ink)}
.feature-card p{margin-top:12px;font-size:11px;line-height:19px;color:var(--muted)}
.feature-card .more{margin-top:12px;font-size:12.5px;color:var(--orange)}

/* about */
.about-bg{left:0;top:1506px;width:1200px;height:935px;background:var(--grey-bg)}
.about-box{left:144px;top:1590px;width:894px;height:739px;background:var(--white);border:1px solid var(--line)}
.about-img{left:0;top:1679px;width:479px;height:562px;background:linear-gradient(170deg,#cfd1c9,#9fa39a 55%,#6d6e66)}
.years{left:346px;top:1701px;width:104px;height:104px;border-radius:50%;text-align:center;color:var(--white)}
.years b{display:block;font-size:50px;font-weight:700;line-height:56px;margin-top:6px}
.years span{display:block;font-size:17px;font-weight:500;line-height:18px}
.about-text{left:580px;top:1716px;width:320px}
.about-text .welcome{font-size:15px;color:var(--ink)}
.about-text h2{font-size:33px;font-weight:500;color:var(--orange);line-height:44px;margin-top:4px}
.about-text .tag{font-size:14px;color:var(--ink)}
.about-text p{font-size:11px;line-height:21px;color:var(--muted);margin-top:22px}
.about-text p + p{margin-top:12px}
.tick-list{list-style:none;margin-top:20px}
.tick-list li{display:flex;align-items:center;gap:18px;font-size:12px;color:var(--ink);height:32.5px}
.tick{width:20px;height:20px;border-radius:50%;display:flex;align-items:center;justify-content:center;box-shadow:0 0 0 3px #fde2d3}
.about-btn{left:583px;top:2196px;width:150px;height:42px;line-height:42px;font-size:15px}
.flame{left:852px;top:2107px;width:157px;height:222px;border-radius:50% 50% 10% 10%;background:linear-gradient(0deg,var(--orange),var(--orange-light))}

/* testimonial */
.testimonial{left:0;top:2441px;width:1200px;height:297px}
.person{left:712px;top:2364px;width:280px;height:374px;border-radius:140px 140px 0 0;background:linear-gradient(180deg,#c99a7e 0%,#2d3340 45%,#1e232c 100%)}
.quote{left:275px;top:2510px;width:440px;color:var(--white)}
.quote .mark{font-size:60px;line-height:40px;font-family:Georgia,serif;height:40px}
.quote p{font-size:13.5px;line-height:22px;margin-top:12px}
.quote .who{margin-top:20px;font-size:19px;font-weight:600}
.nav-dot{width:34px;height:34px;border-radius:50%;display:flex;align-items:center;justify-content:center}

/* contact */
.contact-form{left:254px;top:2927px;width:692px;height:233px;background:var(--white);border-radius:14px;box-shadow:0 0 0 1px #ececec,0 6px 22px rgba(0,0,0,.06)}
.field{width:187px;height:40px;border-radius:8px;background:linear-gradient(180deg,#fff,#f0f0f0);box-shadow:0 2px 5px rgba(0,0,0,.08);font-size:10px;color:var(--muted);padding:13px 16px}
.submit{left:710px;top:3052px;width:187px;height:40px;line-height:40px;font-size:15px;border-radius:22px}
.info{width:240px;text-align:center;font-size:12.5px;line-height:19px;color:var(--ink)}
.info .ico{width:58px;height:58px;margin:0 auto 26px;border-radius:50%;background:var(--white);box-shadow:0 0 0 6px #fbe9df;display:flex;align-items:center;justify-content:center}

/* footer */
.site-footer{left:0;top:3388px;width:1200px;height:212px;background:var(--footer)}
.foot-brand{left:520px;top:3436px;width:160px;text-align:center;color:var(--orange);font-weight:600;font-size:15px}
.foot-links{left:200px;top:3488px;display:flex;gap:10px;font-size:10.5px;color:#b9c0c8}
.foot-copy{left:718px;top:3488px;font-size:10px;color:#b9c0c8}
.social{left:589px;top:3523px;width:32px;height:32px;border-radius:50%;background:var(--orange)}
</style>
</head>
<body>

<header class="abs site-header">
  <div class="abs brand"><span class="brand-dot"></span><br>HAVEN &amp; RESTORE<small>SERVICES</small></div>
  <nav class="abs main-nav">
    <span class="active">HOME</span><span>ABOUT US</span><span>SERVICES &#9662;</span><span>TESTIMONIALS</span><span>CONTACT US</span>
  </nav>
</header>
<div class="abs call-box grad" style="z-index:3"><span class="lbl">Call Us On Today :</span><span class="num">0400 123 456</span></div>
<div class="abs call-icon" style="z-index:4">
  <svg width="22" height="22" viewBox="0 0 24 24"><path d="M6.6 10.8a15 15 0 0 0 6.6 6.6l2.2-2.2a1 1 0 0 1 1-.25 11.4 11.4 0 0 0 3.6.57 1 1 0 0 1 1 1V20a1 1 0 0 1-1 1A17 17 0 0 1 3 4a1 1 0 0 1 1-1h3.5a1 1 0 0 1 1 1c0 1.25.2 2.45.57 3.57a1 1 0 0 1-.25 1z" fill="#f26522"/></svg>
</div>

<section class="abs hero" role="img" aria-label="Photo of a technician in a respirator mask and overalls standing in a cleaned living room"></section>
<div class="abs hero-badge">
  <div class="pre">We're Here To <b>Help.</b></div>
  <h1>24/7 CRIME SCENE<br>&amp; TRAUMA CLEANUP</h1>
  <span class="btn">Contact Us</span>
</div>
<svg class="abs hero-arrows" width="80" height="16" viewBox="0 0 80 16"><path d="M2 8h34M2 8l5-4M2 8l5 4" stroke="#fff" stroke-width="1.2" fill="none"/><path d="M44 8h34M78 8l-5-4M78 8l-5 4" stroke="#f26522" stroke-width="1.2" fill="none"/></svg>

<h2 class="abs sec-title" style="top:780px">SERVICES WE PROVIDE</h2>
<p class="abs sec-sub" style="top:832px">Lorem Ipsum is simply dummy text of the printing typesetti industry the<br>Lorem Ipsum has been the industry.</p>

<div class="abs service on" style="left:160px;top:912px" role="img" aria-label="Fire icon"><div class="ring"><span></span></div>Fire &amp; Smoke<br>Restoration</div>
<div class="abs service" style="left:337px;top:912px" role="img" aria-label="Water pipe icon"><div class="ring"><span></span></div>Water Restoration/<br>Mould Remediation</div>
<div class="abs service" style="left:516px;top:912px" role="img" aria-label="Crime scene tape icon"><div class="ring"><span></span></div>Crime Scene<br>Cleaners</div>
<div class="abs service" style="left:693px;top:912px" role="img" aria-label="Hoarding clutter icon"><div class="ring"><span></span></div>Hoarding &amp;<br>Squalor Cleaning</div>
<div class="abs service" style="left:871px;top:912px" role="img" aria-label="Crystal icon"><div class="ring"><span></span></div>Methamphetamine<br>Remediation/ Testing<br>Services</div>
<div class="abs services-rule"></div>
<div class="abs services-active"></div>

<div class="abs feature-img" role="img" aria-label="Photo of a fire damaged kitchen"></div>
<div class="abs feature-tag">FIRE RESTORATION</div>
<article class="abs feature-card">
  <h3>Fire &amp; Smoke Restoration</h3>
  <p>Lorem Ipsum is simply dummy text of the printing typesetti industry. Lorem Ipsum has been the industry's standard dummy text ever.</p>
  <div class="more">Read More &#9656;</div>
</article>

<section class="abs about-bg"></section>
<div class="abs about-box"></div>
<div class="abs about-img" role="img" aria-label="Photo of a flooded living room"></div>
<div class="abs years grad"><b>14</b><span>Years</span></div>
<div class="abs about-text">
  <div class="welcome">Welcome To</div>
  <h2>HAVEN &amp; RESTORE</h2>
  <div class="tag">Cleaning &amp; Property Maintenance Specialist</div>
  <p>Lorem Ipsum is simply dummy text of the printing typesetti industry. Lorem Ipsum has been the indu stry's standard dummy text ever since the when is an unknown printer took a the galley.</p>
  <p>Lorem Ipsum is simply dummy text of the printing typesetti industry. Lorem Ipsum has been the indu stry's standard dummy text ever.</p>
  <ul class="tick-list">
    <li><span class="tick grad"><svg width="8" height="8" viewBox="0 0 8 8"><path d="M2.5 1l3 3-3 3" stroke="#fff" stroke-width="1.5" fill="none"/></svg></span>Fire &amp; Smoke Restoration</li>
    <li><span class="tick grad"><svg width="8" height="8" viewBox="0 0 8 8"><path d="M2.5 1l3 3-3 3" stroke="#fff" stroke-width="1.5" fill="none"/></svg></span>Water Restoration/ Mould Remediation</li>
    <li><span class="tick grad"><svg width="8" height="8" viewBox="0 0 8 8"><path d="M2.5 1l3 3-3 3" stroke="#fff" stroke-width="1.5" fill="none"/></svg></span>Crime Scene Cleaners</li>
    <li><span class="tick grad"><svg width="8" height="8" viewBox="0 0 8 8"><path d="M2.5 1l3 3-3 3" stroke="#fff" stroke-width="1.5" fill="none"/></svg></span>Hoarding &amp; Squalor Cleaning</li>
    <li><span class="tick grad"><svg width="8" height="8" viewBox="0 0 8 8"><path d="M2.5 1l3 3-3 3" stroke="#fff" stroke-width="1.5" fill="none"/></svg></span>Hoarding &amp; Squalor Cleaning</li>
  </ul>
</div>
<span class="abs btn grad about-btn">Contact Us</span>
<div class="abs flame" role="img" aria-label="Illustration of an orange flame"></div>

<section class="abs testimonial grad"></section>
<div class="abs person" role="img" aria-label="Photo of a smiling client in a suit with arms crossed"></div>
<div class="abs nav-dot" style="left:64px;top:2540px;background:var(--ink)"><svg width="10" height="10" viewBox="0 0 10 10"><path d="M6.5 1.5L3 5l3.5 3.5" stroke="#fff" stroke-width="1.4" fill="none"/></svg></div>
<div class="abs nav-dot" style="left:60px;top:2580px;width:42px;height:42px;border:1.5px solid #fff"><svg width="10" height="10" viewBox="0 0 10 10"><path d="M3.5 1.5L7 5 3.5 8.5" stroke="#fff" stroke-width="1.4" fill="none"/></svg></div>
<blockquote class="abs quote">
  <div class="mark">&#8220;&#8220;</div>
  <p>"Daniel Voskuil professionalism combined with their calm, friendly attitude makes them a joy to be with. Thank you Daniel Voskuil. "</p>
  <div class="who">&mdash;&nbsp; R. Elmsworth</div>
</blockquote>

<h2 class="abs sec-title" style="top:2815px">CONTACT US</h2>
<p class="abs sec-sub" style="top:2866px;font-size:14px">If you have an any Question for contact us Today :</p>
<form class="abs contact-form"></form>
<div class="abs field" style="left:305px;top:2997px">First Name *</div>
<div class="abs field" style="left:507px;top:2997px">Last Name*</div>
<div class="abs field" style="left:710px;top:2997px">Phone *</div>
<div class="abs field" style="left:305px;top:3052px">Email*</div>
<div class="abs field" style="left:507px;top:3052px">Message *</div>
<span class="abs btn grad submit">Submit</span>

<div class="abs info" style="left:252px;top:3209px"><div class="ico"><svg width="18" height="22" viewBox="0 0 18 22"><path d="M9 1a7 7 0 0 1 7 7c0 5-7 13-7 13S2 13 2 8a7 7 0 0 1 7-7z" fill="none" stroke="#f26522" stroke-width="1.8"/><circle cx="9" cy="8" r="2.5" fill="#f26522"/></svg></div>12 Wattle Lane<br>Springfield QLD 4300</div>
<div class="abs info" style="left:495px;top:3209px"><div class="ico" style="background:var(--orange)"><svg width="18" height="14" viewBox="0 0 18 14"><rect x="1" y="1" width="16" height="12" rx="1" fill="#fff"/><path d="M1 2l8 6 8-6" stroke="#f26522" stroke-width="1.4" fill="none"/></svg></div>hello@havenrest<br>ore.com.au</div>
<div class="abs info" style="left:734px;top:3209px"><div class="ico"><svg width="20" height="20" viewBox="0 0 24 24"><path d="M6.6 10.8a15 15 0 0 0 6.6 6.6l2.2-2.2a1 1 0 0 1 1-.25 11.4 11.4 0 0 0 3.6.57 1 1 0 0 1 1 1V20a1 1 0 0 1-1 1A17 17 0 0 1 3 4a1 1 0 0 1 1-1h3.5a1 1 0 0 1 1 1c0 1.25.2 2.45.57 3.57a1 1 0 0 1-.25 1z" fill="#f26522"/></svg></div>Phone:<br>0400 123 456</div>

<footer class="abs site-footer"></footer>
<div class="abs foot-brand">HAVEN &amp; RESTORE</div>
<nav class="abs foot-links"><span>Home</span><span>About Us</span><span>Services</span><span>Testimonials</span><span>Contact Us</span></nav>
<div class="abs foot-copy">&copy;HAVEN &amp; RESTORE SERVICES - 2020 All rights reserved.</div>
<div class="abs social" role="img" aria-label="Social media link"></div>

</body>
</html>
```